Website Design for Circuit Haven

We provide Instore and in-house computer services for SOHO, Medium and Enterprise customers. Supplying Cloud Services, Servers, Computers, Tablets, Phones and other IT products. We repair Kestrel Printers as an authorised repair agent. Looking for a site

```html
<!DOCTYPE html>
<html lang="en">
<head>
<meta charset="utf-8">
<title>Circuit Haven</title>
<link rel="stylesheet" href="https://fonts.googleapis.com/css2?family=Arimo:wght@700&family=Arvo&family=Anonymous+Pro&display=swap">
<style>
:root{
  --red:#e31b23;
  --red-dark:#c9141b;
  --ink:#1d1d1d;
  --text:#2a2a2a;
  --muted:#555;
  --band:#e6e6e6;
  --card:#ffffff;
  --map-base:#e9e5dc;
  --map-road:#f3e88a;
}
*{margin:0;padding:0;box-sizing:border-box}
html,body{width:1171px;height:1200px;overflow:hidden;background:#fff}
.page{position:relative;width:1171px;height:1200px;font-family:"Anonymous Pro",monospace;color:var(--text)}
.brand{position:absolute;left:137px;top:112px;display:flex;align-items:center;gap:18px}
.brand-name{font-family:"Arvo",serif;font-size:54px;color:var(--ink);letter-spacing:1px}
.brand-dot{width:46px;height:46px;border-radius:50%;background:var(--red)}
.nav{position:absolute;top:242px;left:0;width:100%;height:20px}
.nav a{position:absolute;font-family:"Arimo",sans-serif;font-weight:700;font-size:14.5px;color:var(--ink);text-decoration:none;letter-spacing:.3px}
.rule{position:absolute;left:0;width:100%;height:7px;background:var(--red)}
.rule.top{top:283px}
.rule.bottom{top:721px}
.band{position:absolute;left:0;top:290px;width:100%;height:431px;background:var(--band)}
.map-card{position:absolute;left:122px;top:319px;width:238px;height:215px;background:var(--card);border-radius:8px}
.map{position:absolute;left:15px;top:16px;width:208px;height:181px;background:linear-gradient(160deg,var(--map-base) 0%,#dfe6d2 45%,var(--map-base) 60%,#f0ebc4 100%)}
.map-link{position:absolute;left:0;top:195px;width:100%;text-align:center;font-family:"Arimo",sans-serif;font-size:12px;font-weight:400;color:var(--muted)}
.address{position:absolute;left:122px;top:545px;width:238px;text-align:center;font-family:Arial,"Arimo",sans-serif;font-size:11.5px;line-height:22.7px;color:var(--muted)}
.intro{position:absolute;left:445px;top:319px;width:591px;height:348px;background:var(--card);border-radius:8px;text-align:center}
.intro h1{font-family:"Arvo",serif;font-weight:400;font-size:17px;line-height:20px;color:var(--ink);margin-top:24px;letter-spacing:.4px}
.intro p{font-size:13.5px;line-height:17.3px;margin-top:17px;color:var(--text)}
.intro p:first-of-type{margin-top:18px}
.cta{position:absolute;left:204px;top:282px;width:194px;height:41px;border-radius:8px;background:linear-gradient(#f33b41,var(--red-dark));color:#fff;font-family:"Arimo",sans-serif;font-weight:700;font-size:12.5px;line-height:41px;letter-spacing:.6px;text-decoration:none;box-shadow:0 2px 3px rgba(0,0,0,.2)}
.col{position:absolute;top:757px}
.col h2{font-family:"Arvo",serif;font-weight:400;font-size:14.5px;line-height:22.5px;color:var(--ink);text-align:center;letter-spacing:.3px}
.col ul{list-style:none;margin-top:30px}
.col li{font-size:12.5px;line-height:22.7px;color:var(--text);padding-left:10px;text-indent:-10px}
.col-problems{left:141px;width:250px}
.col-laptop{left:453px;width:265px}
.col-laptop h2{margin-left:-5px}
.col-brands{left:785px;width:228px}
.col-brands h2{margin-top:0}
.badges{display:grid;grid-template-columns:repeat(3,1fr);gap:14px 14px;margin-top:40px}
.badge{height:32px;border-radius:4px;background:#d4d8de}
.badge.red{background:#e7b3b5}
.badge.blue{background:#b9c6df}
.badge.green{background:#c9dcb0}
</style>
</head>
<body>
<div class="page">
  <header>
    <div class="brand">
      <span class="brand-name">Circuit Haven</span>
      <span class="brand-dot"></span>
    </div>
    <nav class="nav">
      <a href="#" style="left:141px">HOME</a>
      <a href="#" style="left:200px">ABOUT US</a>
      <a href="#" style="left:294px">SERVICES</a>
      <a href="#" style="left:385px">CONTACT US</a>
      <a href="#" style="left:500px">REMOTE SUPPORT</a>
    </nav>
  </header>

  <div class="rule top"></div>
  <section class="band">
  </section>
  <div class="rule bottom"></div>

  <div class="map-card">
    <div class="map" role="img" aria-label="Street map showing the workshop location"></div>
    <span class="map-link">See the full map</span>
  </div>
  <address class="address" style="font-style:normal">
    Harbourside Arcade<br>
    Shop 4 / 112-114 Larkspur Road,<br>
    Maple Heights<br>
    Phone: (07) 5550 1234<br>
    Email: &nbsp;info@circuithaven.example
  </address>

  <article class="intro">
    <h1>Our workshops are fully equipped to service, repair &amp;<br>optimise your computer!</h1>
    <p>A combination of industry leading technology and highly skilled staff mean<br>your PC won't be waiting for a week or two to be repaired.<br>Typical turn around is 24 hours, with large jobs or major rebuilds<br>taking up to 48 hours.</p>
    <p>Enjoy a face to face relationship with our technicians, who will<br>guide you through your computer service to ensure<br>it is a smooth, fast and stress-free process.</p>
    <p>With strict data management procedures you can feel confident<br>that your data will be handled with 100% priority and confidentiality.</p>
    <a class="cta" href="#">FIX MY COMPUTER</a>
  </article>

  <section class="col col-problems">
    <h2>Some of the computer problems<br>we repair on a regular basis:</h2>
    <ul>
      <li>- Computer not posting</li>
      <li>- Computer not booting</li>
      <li>- Computer freezing</li>
      <li>- No signal on monitor</li>
      <li>- Blue screens of death (BSOD)</li>
      <li>- Viruses, trojans, malware &amp; spyware</li>
      <li>- Faulty hard drive</li>
      <li>- Faulty RAM (memory)</li>
      <li>- Faulty motherboard</li>
    </ul>
  </section>

  <section class="col col-laptop">
    <h2>Some of the most common faults we<br>come across in laptop include:</h2>
    <ul>
      <li>- Smashed, broken or cracked LCD screens (or LED)</li>
      <li>- Missing keys or water damaged, unresponsive, broken or faulty keyboards</li>
      <li>- Black or blank screen when laptop is turned on</li>
      <li>- Laptop not charging</li>
      <li>- Broken DC power/charger jack</li>
      <li>- Laptop battery not charging / holding charge</li>
      <li>- Loud fans</li>
      <li>- Overheating</li>
    </ul>
  </section>

  <section class="col col-brands">
    <h2>We Repair All Computers</h2>
    <div class="badges">
      <div class="badge blue"></div>
      <div class="badge red"></div>
      <div class="badge red"></div>
      <div class="badge"></div>
      <div class="badge blue"></div>
      <div class="badge"></div>
      <div class="badge blue"></div>
      <div class="badge green"></div>
      <div class="badge"></div>
      <div class="badge blue"></div>
      <div class="badge"></div>
      <div class="badge blue"></div>
    </div>
  </section>
</div>
</body>
</html>
```